Velanqua Cookbook (Independant Velanqua Consultant - not Velanqua themselves)

Approx 120 page Recipe book, need design created for recipe pages.
each recipe illustrated with full colour photograph (supplied) on opposite page.
To included index, contents page, intro, etc
Cover design also to be suggested.
We must have a professional finish, but with a friendly, family theme.
Reason: Deadline extended because I require further designs, please.

```html
<!DOCTYPE html>
<html lang="en">
<head>
<meta charset="utf-8">
<title>Velanqua Cookbook – Recipe Spreads</title>
<link rel="stylesheet" href="https://fonts.googleapis.com/css2?family=Arimo:ital,wght@0,400;0,700;1,400&family=Josefin+Sans:wght@300;600&display=swap">
<style>
  :root {
    --page: #edf1ec;
    --red: #c0191f;
    --ink: #1d1d1d;
    --band: #1b1a18;
    --gutter: #9a9d99;
    --muted: #555;
  }
  * { margin: 0; padding: 0; box-sizing: border-box; }
  html, body { width: 683px; height: 1200px; overflow: hidden; background: var(--page); }
  body { font-family: "Arimo", Arial, sans-serif; color: var(--ink); }

  .spread { position: relative; width: 683px; height: 388px; background: var(--page); overflow: hidden; }
  .spread::after {
    content: ""; position: absolute; left: 342px; top: 0; bottom: 0;
    width: 1px; background: var(--gutter);
  }
  .band { height: 17px; background: var(--band); }

  .recipe-title {
    position: absolute; left: 26px;
    font-weight: 700; font-size: 13.6px; line-height: 16px; color: var(--red);
    white-space: nowrap;
  }
  .tagline {
    position: absolute; left: 26px;
    font-family: "Josefin Sans", sans-serif; font-weight: 600; font-size: 9.5px; color: var(--red);
  }
  .ingredients {
    position: absolute; left: 26px;
    display: grid; grid-template-columns: 133px 150px;
    font-style: italic; font-size: 8.2px; line-height: 12.1px;
  }
  .ingredients .sub-heading { color: var(--red); }
  .method { position: absolute; left: 26px; font-size: 8.2px; line-height: 12.2px; }
  .method h3 { font-size: 8.2px; line-height: 12.2px; font-weight: 700; color: var(--red); margin: 10px 0 3px; }
  .method h3:first-child { margin-top: 0; }

  .page-foot {
    position: absolute; left: 26px;
    font-family: "Josefin Sans", sans-serif; font-weight: 300; font-size: 11px;
    display: flex; gap: 14px; color: var(--muted);
  }
  .page-foot .section { color: var(--red); letter-spacing: 0.5px; }
  .page-num-right {
    position: absolute; left: 646px;
    font-family: "Josefin Sans", sans-serif; font-weight: 300; font-size: 11px; color: var(--muted);
  }
  .diet-tags {
    position: absolute;
    font-family: "Josefin Sans", sans-serif; font-weight: 600; font-size: 8px;
    color: var(--red); display: flex; gap: 9px; align-items: flex-start;
  }
  .diet-tags .low { margin-top: 8px; }

  .photo {
    position: absolute; left: 352px; width: 320px; height: 215px;
    border-radius: 2px;
  }
  .photo-trout { background: radial-gradient(ellipse at 40% 60%, #b9c2a8 0%, #8e8a78 45%, #6f6558 100%); }
  .photo-salad { background: radial-gradient(ellipse at 55% 55%, #c8a46a 0%, #e9e6e0 35%, #d7d4d6 70%, #b54a3a 100%); }
  .photo-ice { background: radial-gradient(ellipse at 48% 55%, #d96a8c 0%, #c98fa4 30%, #b5b8b8 65%, #9da1a0 100%); }
</style>
</head>
<body>

<section class="spread">
  <h2 class="recipe-title" style="top:46px">STEAMED TROUT WITH PARSLEY BUTTER</h2>
  <div class="ingredients" style="top:80px">
    <span>1 trout</span><span class="sub-heading">for Parsley Butter</span>
    <span>½ lemon</span><span>60g butter</span>
    <span>2 cloves garlic</span><span>1 teaspoon lemon rind, grated</span>
    <span>Salt and pepper</span><span>1 tablespoon parsley</span>
    <span>Parsley butter</span><span>1 tablespoon lemon juice</span>
  </div>
  <div class="method" style="top:158px">
    <h3>To make parsley butter</h3>
    <p>Place all ingredients in clean, dry bowl and mix for 15 seconds, Speed 5.</p>
    <p>Roll into logs and refrigerate, or just place in small dish to serve.</p>
    <h3>To cook steamed trout</h3>
    <p>Slice lemon.</p>
    <p>Peel and chop garlic.</p>
    <p>Fill trout with lemon, garlic, salt and pepper.</p>
    <p>Place in Vapora tray.</p>
    <p>Fill bowl with 700g water.</p>
    <p>Steam 20 minutes, Vapora temperature, Speed 4.</p>
    <h3>To serve</h3>
    <p>Serve with Parsley Butter.</p>
  </div>
  <div class="page-foot" style="top:366px"><span>2</span><span class="section">SEA FOOD</span></div>
  <div class="diet-tags" style="left:492px;top:358px"><span>EF</span><span class="low">V</span><span>GF</span></div>
  <div class="page-num-right" style="top:366px">3</div>
  <div class="photo photo-trout" style="top:86px" role="img" aria-label="Photo of whole steamed trout on lettuce with lemon slices and a dish of parsley butter"></div>
</section>
<div class="band"></div>

<section class="spread">
  <h2 class="recipe-title" style="top:47px">RED CAPSICUM AND BROCCOLI SALAD</h2>
  <div class="ingredients" style="top:79px;grid-template-columns:200px">
    <span>3 rashers bacon</span>
    <span>1 red pepper</span>
    <span>½ small red onion</span>
    <span>1 head broccoli</span>
    <span>45g cranberries or sultanas</span>
    <span>30g slivered almonds</span>
    <span>French Dressing</span>
  </div>
  <div class="method" style="top:180px">
    <h3>To cook</h3>
    <p>Cut red pepper and onion into pieces and add to bowl.</p>
    <p>Chop for 3 seconds on Speed 4.</p>
    <p>Cut broccoli into florets.&nbsp; Add to bowl with cranberries and almonds.</p>
    <p>Chop 5 seconds, Speed 4 or until chopped to desired size.</p>
    <p>Place in serving bowl and drizzle with dressing</p>
    <h3>To serve</h3>
    <p>Chop bacon into large pieces. Pan fry until crisp. Place into VQ bowl.</p>
  </div>
  <div class="page-foot" style="top:366px"><span>4</span><span class="section">VEGETABLES AND SALAD</span></div>
  <div class="diet-tags" style="left:487px;top:368px"><span>GF</span><span>DF</span><span>EF</span></div>
  <div class="page-num-right" style="top:366px">5</div>
  <div class="photo photo-salad" style="top:86px" role="img" aria-label="Photo of chopped broccoli and capsicum salad in a white bowl surrounded by red peppers and broccoli"></div>
</section>
<div class="band"></div>

<section class="spread">
  <h2 class="recipe-title" style="top:50px">DREAMY RASPBERRY DELIGHT</h2>
  <p class="tagline" style="top:69px">Another ice cream made in next to no time!</p>
  <div class="ingredients" style="top:97px;grid-template-columns:200px">
    <span>400g frozen raspberries</span>
    <span>1 tin sweetened condensed milk</span>
    <span>130g cream</span>
    <span>30g lemon juice</span>
    <span>30g sugar</span>
  </div>
  <div class="method" style="top:167px">
    <h3>To make dreamy raspberry delight</h3>
    <p>Mix for 1 minute on Speed 8 until smooth.</p>
    <p>Transfer to plastic container and freeze 4 hours or until solid.</p>
    <p>Soften slightly before serving.</p>
    <h3>To serve</h3>
    <p>Place all ingredients in bowl.</p>
  </div>
  <div class="page-foot" style="top:370px"><span>6</span><span class="section">ICE CREAM DELIGHT</span></div>
  <div class="diet-tags" style="left:490px;top:372px"><span>EF</span><span style="margin-left:14px">GF</span></div>
  <div class="page-num-right" style="top:370px">7</div>
  <div class="photo photo-ice" style="top:94px;height:212px" role="img" aria-label="Photo of raspberry ice cream in a glass topped with raspberries and a spoon"></div>
</section>

</body>
</html>
```